Business Card Design

We are a project managment company specializing in Interior fitout
VRK is for Commercial, Domestic, Industial - we provide managment to these industries and see the projects through design to contruction
Would like an area on the back of the card where peoplr can write notes
Thinking laser lines and architectural finishes
Colour theme at the moment is light grey and red although im open to any colour/design scheme

VRK Ventures
Lewis Prentham
Managing Director
0419582147
lewis@vrkventures.com.au

```html
<!DOCTYPE html>
<html lang="en">
<head>
<meta charset="utf-8">
<title>VRK Ventures – Business Card</title>
<link rel="stylesheet" href="https://fonts.googleapis.com/css2?family=Mulish:wght@300;400;500;600&display=swap">
<style>
  :root {
    --backdrop: #e8e8e8;
    --brand-orange: #f2791e;
    --card-edge: #8a8a8a;
    --back-grey: #b1b6b9;
    --drawing-dark: #7e8489;
    --drawing-mid: #9aa0a4;
    --drawing-light: #aab0b3;
    --rule: #6f7478;
    --ink: #111111;
    --white: #ffffff;
  }
  * { margin: 0; padding: 0; box-sizing: border-box; }
  html, body {
    width: 1200px; height: 741px; overflow: hidden;
    background: var(--backdrop);
    font-family: "Mulish", Arial, sans-serif;
  }
  .canvas { position: relative; width: 1200px; height: 741px; }
  .card {
    position: absolute;
    width: 569px; height: 335px;
    border-radius: 32px;
    border: 1px solid var(--card-edge);
    overflow: hidden;
  }
  .card-front {
    left: 46px; top: 27px;
    background: var(--brand-orange);
    display: flex; align-items: center; justify-content: center;
  }
  .brand-name {
    color: var(--white);
    font-weight: 300;
    font-size: 40px;
    letter-spacing: 4px;
    margin-top: -4px;
  }
  .card-back {
    left: 568px; top: 383px;
    background: var(--back-grey);
  }
  .drawing-area { position: absolute; left: 0; top: 0; width: 569px; height: 335px; }
  .contact-name {
    position: absolute; left: 168px; top: 106px;
    font-size: 22px; font-weight: 400; color: var(--ink);
    letter-spacing: 0.3px;
  }
  .contact-name .given { font-weight: 600; }
  .contact-line {
    position: absolute; left: 168px;
    display: flex; align-items: center; gap: 7px;
    font-size: 14.5px; color: var(--ink);
  }
  .contact-line svg { width: 13px; height: 13px; flex: none; }
  .contact-phone { top: 162px; }
  .contact-email { top: 185px; }
  .divider {
    position: absolute; left: 487px; top: 31px;
    width: 1px; height: 275px; background: var(--rule);
  }
  .sectors {
    position: absolute; left: 500px; top: 306px;
    transform: rotate(-90deg); transform-origin: left top;
    width: 275px;
    font-size: 15.5px; line-height: 25px; color: var(--ink);
    text-align: center; white-space: nowrap;
  }
</style>
</head>
<body>
<div class="canvas">
  <section class="card card-front">
    <div class="brand-name">VRK Ventures</div>
  </section>

  <section class="card card-back">
    <svg class="drawing-area" viewBox="0 0 569 335" role="img" aria-label="Architectural floor plan line drawing framing the top, left and bottom edges of the card">
      <defs>
        <linearGradient id="planTone" x1="0" y1="0" x2="1" y2="1">
          <stop offset="0" stop-color="var(--drawing-dark)"/>
          <stop offset="0.6" stop-color="var(--drawing-mid)"/>
          <stop offset="1" stop-color="var(--drawing-light)"/>
        </linearGradient>
      </defs>
      <path d="M0 0 H243 L225 22 L165 40 L120 48 L95 80 L80 120 L72 165 L82 210 L95 240 L160 232 L250 236 L300 248 L330 262 L335 335 H0 Z" fill="url(#planTone)"/>
    </svg>

    <div class="contact-name"><span class="given">Lewis</span> Prentham</div>
    <div class="contact-line contact-phone">
      <svg viewBox="0 0 16 16"><path d="M2 6c0-3 12-3 12 0v1.5h-3V6H5v1.5H2Z M4 8h8l1.5 6h-11Z" fill="#111"/><circle cx="8" cy="11" r="1.8" fill="#b1b6b9"/></svg>
      <span>0419582147</span>
    </div>
    <div class="contact-line contact-email">
      <svg viewBox="0 0 16 16"><path d="M15 1 1 7l5 2 1.5 6L10 10l4 2Z" fill="#111"/></svg>
      <span>lewis@vrkventures.com.au</span>
    </div>

    <div class="divider"></div>
    <div class="sectors">
      Commercial ▪ Domestic ▪ Industrial<br>Interiors and Construction
    </div>
  </section>
</div>
</body>
</html>
```